VELOTRA Brisbane Tiling Service

My name is Milos Vrenbek i need a business card for a new company. We are wall and floor tilers based in Brisbane, our company is Velotra Brisbane Tiling Service.
We would like a logo from our website used on our cards. Our website is www.velotra-tiles.com.au

I would like my Facebook and Twitter accounts on my card.

Business

Colors
0692cd
3176b5
33a6d7
85cae6

```html
<!DOCTYPE html>
<html lang="en">
<head>
<meta charset="utf-8">
<title>Velotra Brisbane Tiling Service – Business Card</title>
<link rel="stylesheet" href="https://fonts.googleapis.com/css2?family=Mulish:wght@400;700&display=swap">
<style>
  :root {
    --backdrop: #e9ebee;
    --card: #ffffff;
    --ink: #1a1a1a;
    --brand-blue: #3176b5;
    --brand-deep: #2a6fb4;
    --brand-sky: #33a6d7;
    --brand-pale: #85cae6;
    --divider: #dfe3e8;
  }
  * { margin: 0; padding: 0; box-sizing: border-box; }
  html, body {
    width: 1200px; height: 1000px; overflow: hidden;
    background: var(--backdrop);
    font-family: "Mulish", "Century Gothic", sans-serif;
    color: var(--ink);
  }
  .card {
    position: absolute; left: 265px; width: 665px; height: 397px;
    background: var(--card);
    box-shadow: 0 3px 10px rgba(0,0,0,0.18);
    overflow: hidden;
  }
  .card--front { top: 73px; }
  .card--back { top: 533px; }

  .brand-mark {
    position: absolute;
    background: linear-gradient(135deg, var(--brand-sky), var(--brand-blue));
  }
  .card--front .brand-mark { left: 95px; top: 80px; width: 142px; height: 147px; }
  .card--back .brand-mark { left: 242px; top: 47px; width: 183px; height: 187px; }

  .brand-name {
    position: absolute; left: 0; text-align: center;
    font-weight: 400; color: var(--ink); letter-spacing: 2px;
  }
  .brand-tagline {
    position: absolute; left: 0; text-align: center;
    color: var(--brand-blue); font-weight: 400;
  }
  .card--front .brand-name { top: 240px; width: 333px; font-size: 42px; }
  .card--front .brand-tagline { top: 288px; width: 333px; font-size: 22px; }
  .card--back .brand-name { top: 250px; width: 665px; font-size: 56px; }
  .card--back .brand-tagline { top: 315px; width: 665px; font-size: 30px; }

  .divider {
    position: absolute; left: 322px; top: 72px; width: 1px; height: 260px;
    background: var(--divider);
  }

  .contact { position: absolute; left: 338px; top: 74px; font-size: 16.5px; line-height: 1.4; }
  .contact__name { color: var(--brand-blue); font-weight: 700; font-size: 20px; line-height: 1.1; }
  .contact__role { font-size: 17px; line-height: 1.2; margin-bottom: 10px; }
  .contact__label { color: var(--brand-blue); font-weight: 700; }
  .contact__group { margin-bottom: 6px; }
  .contact__social { display: flex; align-items: center; gap: 6px; margin-top: 10px; line-height: 1.65; }
  .contact__social + .contact__social { margin-top: 0; }
  .social-square { width: 17px; height: 17px; background: var(--brand-deep); display: inline-block; }

  .front-band {
    position: absolute; left: 0; bottom: 0; width: 100%; height: 33px;
    background: linear-gradient(90deg, var(--brand-deep) 0%, var(--brand-blue) 35%, var(--brand-pale) 60%, var(--brand-blue) 80%, var(--brand-deep) 100%);
  }
</style>
</head>
<body>
  <section class="card card--front">
    <div class="brand-mark"></div>
    <div class="brand-name">VELOTRA</div>
    <div class="brand-tagline">Brisbane Tiling Service</div>

    <div class="divider"></div>

    <div class="contact">
      <div class="contact__name">Milos Vrenbek</div>
      <div class="contact__role">Founder</div>
      <div class="contact__group">
        <div><span class="contact__label">Abn:</span> 51824630972</div>
        <div><span class="contact__label">Qbcc:</span> 1093546</div>
      </div>
      <div>
        <div><span class="contact__label">Tel:</span> 0411 555 018</div>
        <div><span class="contact__label">Tel:</span> 07 3555 0142</div>
        <div><span class="contact__label">Email:</span> info@velotra-tiles.com.au</div>
      </div>
      <div class="contact__social"><span class="social-square"></span>@Infovelotra</div>
      <div class="contact__social"><span class="social-square"></span>Velotra - Brisbane Tiling Service</div>
    </div>

    <div class="front-band"></div>
  </section>

  <section class="card card--back">
    <div class="brand-mark"></div>
    <div class="brand-name">VELOTRA</div>
    <div class="brand-tagline">Brisbane Tiling Service</div>
  </section>
</body>
</html>
```